Real Estate "For Sale" Sign for a Colorado Real Estate Company

I need a sign for my Real Estate Company and the size needs to be 24inches by 24inches when printed on metal.
Logo is attached and would like to keep it modern and simple. We are a small town and I am not looking for a new age, industrial design. The concept needs to have the following attributes:

- Logo placed on sign
- Text "For Sale"
- Text "Wade Pellman" and my phone number "720-381-6072" (I would need any font package you use so that I can edit my number if that changes)
- Text "www.wade-pellman.example"
Im open to other attributes as well!

Target Market(s)

General Public driving around town.

Industry/Entity Type

Real Estate Agent

Requirements
Must have
• Logo and the colors must not be too busy. Contact Info very clear.

```html
<!DOCTYPE html>
<html lang="en">
<head>
<meta charset="utf-8">
<title>Elk Meadow Realty – For Sale Sign</title>
<link rel="stylesheet" href="https://fonts.googleapis.com/css2?family=Cinzel:wght@600;700&family=Open+Sans:wght@600;700&display=swap">
<style>
  :root {
    --navy: #17476b;
    --brand-blue: #1080c2;
    --ink-gray: #464646;
    --swoosh-black: #1e1e1e;
    --sign-white: #ffffff;
  }
  html, body {
    margin: 0;
    padding: 0;
    width: 1188px;
    height: 1200px;
    overflow: hidden;
    background: var(--sign-white);
  }
  .sign {
    position: relative;
    width: 1188px;
    height: 1200px;
    background: var(--sign-white);
    overflow: hidden;
  }
  .sign__waves {
    position: absolute;
    inset: 0;
    width: 1188px;
    height: 1200px;
  }
  .brand {
    position: absolute;
    top: 210px;
    left: 0;
    width: 100%;
    text-align: center;
    color: var(--navy);
    font-family: "Cinzel", serif;
    font-weight: 700;
  }
  .brand__name {
    display: block;
    font-size: 98px;
    line-height: 1;
    letter-spacing: 1px;
  }
  .brand__suffix {
    display: block;
    margin-top: 14px;
    font-size: 34px;
    letter-spacing: 18px;
    padding-left: 18px;
  }
  .headline {
    position: absolute;
    top: 465px;
    left: 0;
    width: 100%;
    margin: 0;
    text-align: center;
    color: var(--navy);
    font-family: "Cinzel", serif;
    font-weight: 700;
    font-size: 180px;
    line-height: 1;
    letter-spacing: 2px;
  }
  .agent {
    position: absolute;
    top: 730px;
    left: 0;
    width: 100%;
    text-align: center;
    color: var(--navy);
    font-family: "Cinzel", serif;
    font-weight: 700;
    font-size: 100px;
    line-height: 1;
  }
  .phone {
    position: absolute;
    top: 872px;
    left: 0;
    width: 100%;
    display: flex;
    justify-content: center;
    align-items: center;
    gap: 20px;
    color: var(--ink-gray);
    font-family: "Open Sans", sans-serif;
    font-weight: 700;
    font-size: 98px;
    line-height: 1;
    letter-spacing: 1px;
  }
  .phone__icon {
    width: 76px;
    height: 76px;
    flex: none;
  }
  .website {
    position: absolute;
    top: 1117px;
    right: 26px;
    display: flex;
    align-items: center;
    gap: 18px;
    color: var(--sign-white);
    font-family: "Open Sans", sans-serif;
    font-weight: 600;
    font-size: 40px;
    letter-spacing: 4px;
    line-height: 1;
  }
  .website__icon {
    width: 34px;
    height: 34px;
    flex: none;
  }
</style>
</head>
<body>
  <main class="sign">
    <svg class="sign__waves" viewBox="0 0 1188 1200" aria-hidden="true">
      <path d="M0 1158 C 320 1190, 680 1135, 1188 900 L1188 1200 L0 1200 Z" fill="var(--brand-blue)"/>
      <path d="M0 1106 C 220 1160, 520 1168, 835 1070 C 540 1150, 250 1162, 0 1126 Z" fill="var(--swoosh-black)"/>
    </svg>

    <div class="brand">
      <span class="brand__name">Elk Meadow Realty</span>
      <span class="brand__suffix">LLC</span>
    </div>

    <h1 class="headline">For Sale</h1>

    <div class="agent">Wade Pellman</div>

    <div class="phone">
      <svg class="phone__icon" viewBox="0 0 76 76" aria-hidden="true">
        <circle cx="38" cy="38" r="34" fill="none" stroke="var(--brand-blue)" stroke-width="4"/>
        <path d="M30 18 l8 12 -5 5 c2 6 6 10 11 13 l5 -5 9 9 -6 7 c-14 -2 -28 -16 -30 -33 Z" fill="var(--brand-blue)"/>
      </svg>
      <span class="phone__number">720-381-6072</span>
    </div>

    <div class="website">
      <svg class="website__icon" viewBox="0 0 34 34" aria-hidden="true">
        <g fill="none" stroke="var(--sign-white)" stroke-width="2">
          <circle cx="17" cy="17" r="15"/>
          <ellipse cx="17" cy="17" rx="7" ry="15"/>
          <line x1="2" y1="17" x2="32" y2="17"/>
          <line x1="17" y1="2" x2="17" y2="32"/>
          <path d="M5 9 H29 M5 25 H29"/>
        </g>
      </svg>
      <span class="website__url">www.wade-pellman.example</span>
    </div>
  </main>
</body>
</html>
```